Logo & Visitenkarte für Beratung im Bereich Public Affairs, Reputation Management und Strategie
Zielgruppe
Beratung im Bereich Public Affairs, Reputation Management und Strategie. Die Zielgruppe sind Unternehmen und Verbände. Die Firma erreicht für ihre Kunden bei vor allem politischen Stakeholder die strategischen Ziele durch das bessere Argument als die Mitbewerber. Der Weg ist das Ziel.
Aufgabenstellung
Ich habe mich bei der Schreibweise des Namens noch nicht festgelegt; hier kann kreativ mit dem Namen für das Logo gearbeitet werden (z.B. alles klein, Anfangsbuchstabe groß, zusammengeschrieben, auseinander, etc.).
Das Logo soll Professionalität und Durchsetzungsstärke symbolisieren und zugleich Modernität mit einem Hauch Eleganz ausstrahlen. Wir sind ein junges Unternehmen, das dynamisch, agil und digital seine Projekte umsetzt.

```html
<!DOCTYPE html>
<html lang="de">
<head>
<meta charset="utf-8">
<title>The Clearer Case – Visitenkarte</title>
<link href="https://fonts.googleapis.com/css2?family=Montserrat:wght@400;500&display=swap" rel="stylesheet">
<style>
  :root {
    --navy: #074166;
    --paper: #ffffff;
    --backdrop: #c2c1bf;
    --ink: #4a4a4a;
  }
  * { margin: 0; padding: 0; box-sizing: border-box; }
  html, body { width: 1200px; height: 1176px; overflow: hidden; }
  body {
    background: var(--backdrop);
    font-family: "Montserrat", "Helvetica Neue", Arial, sans-serif;
    position: relative;
  }
  .card { position: absolute; width: 770px; height: 488px; }
  .card--front { left: 205px; top: 64px; background: var(--paper); }
  .card--back { left: 196px; top: 638px; background: var(--navy); }

  .brand { position: absolute; display: flex; align-items: center; gap: 14px; font-weight: 500; letter-spacing: 0.04em; text-transform: uppercase; white-space: nowrap; }
  .brand__square { display: block; background: currentColor; }
  .brand--front { left: 20px; top: 56px; color: var(--navy); font-size: 30px; }
  .brand--front .brand__square { width: 26px; height: 26px; }
  .brand--back { left: 0; right: 0; top: 218px; justify-content: center; color: var(--paper); font-size: 44px; gap: 20px; }
  .brand--back .brand__square { width: 38px; height: 38px; }

  .person { position: absolute; left: 386px; top: 168px; width: 300px; text-align: center; color: var(--navy); }
  .person__name { font-size: 41px; font-weight: 400; letter-spacing: 0.02em; line-height: 1; }
  .person__role { margin-top: 20px; font-size: 21px; color: var(--ink); letter-spacing: 0.02em; }

  .address { position: absolute; left: 22px; top: 298px; display: flex; gap: 10px; color: var(--ink); font-size: 19px; line-height: 24px; }
  .address svg { margin-top: -2px; flex: none; }

  .contacts { position: absolute; left: 385px; top: 302px; list-style: none; color: var(--ink); font-size: 19px; }
  .contacts li { display: flex; align-items: center; gap: 10px; height: 28px; margin-bottom: 13px; }
  .contacts svg { width: 24px; height: 24px; flex: none; }
</style>
</head>
<body>
  <section class="card card--front" aria-label="Vorderseite">
    <div class="brand brand--front"><span class="brand__square"></span>The Clearer Case</div>

    <div class="person">
      <h1 class="person__name">YOUR NAME</h1>
      <p class="person__role">JOB POSITION</p>
    </div>

    <div class="address">
      <svg width="22" height="32" viewBox="0 0 22 32" aria-hidden="true"><path d="M11 1C5.5 1 1 5.3 1 10.7 1 18 11 31 11 31s10-13 10-20.3C21 5.3 16.5 1 11 1z" fill="var(--navy)"/><circle cx="11" cy="10.5" r="4" fill="#fff"/></svg>
      <p>Your City Adress<br>Street LocationXXXX,<br>Germany</p>
    </div>

    <ul class="contacts">
      <li><svg viewBox="0 0 24 24" aria-hidden="true"><circle cx="12" cy="12" r="10.5" fill="none" stroke="var(--navy)" stroke-width="2"/><path d="M8 6.5l2 2.6-1.1 1.5c.8 1.7 2 2.9 3.6 3.7l1.5-1.1 2.6 2-1.3 2.1c-4.3-.6-7.6-3.9-8.2-8.2z" fill="var(--navy)"/></svg>+00 000 000 00 000</li>
      <li><svg viewBox="0 0 24 24" aria-hidden="true"><rect x="1" y="5" width="22" height="14" fill="var(--navy)"/><path d="M1.5 5.5L12 13l10.5-7.5M1.5 18.5l8-6.5M22.5 18.5l-8-6.5" fill="none" stroke="#fff" stroke-width="1.2"/></svg>info@The Clearer Case.de</li>
      <li><svg viewBox="0 0 24 24" aria-hidden="true"><g fill="none" stroke="var(--navy)" stroke-width="1.6"><circle cx="12" cy="12" r="10.5"/><ellipse cx="12" cy="12" rx="4.5" ry="10.5"/><path d="M1.5 12h21M3 7h18M3 17h18M12 1.5v21"/></g></svg>www.The Clearer Case.de</li>
    </ul>
  </section>

  <section class="card card--back" aria-label="Rückseite">
    <div class="brand brand--back"><span class="brand__square"></span>The Clearer Case</div>
  </section>
</body>
</html>
```